Speisekarten
Zielgruppe
we run a restaurant and our target groups are families and business people
Aufgabenstellung
The menu consists of a black folder with 8 DIN A4 slots which have a 2 cm border on all sides. The card should be discreet, classy and easy to read without any kind of complicated fonts or pictures. we would like to see creative designs regarding our recommendation at the end of page 3.

```html
<!DOCTYPE html>
<html lang="de">
<head>
<meta charset="utf-8">
<title>Nazanin – Aperitif</title>
<link href="https://fonts.googleapis.com/css2?family=Poppins:wght@300;400;600;700&family=Bodoni+Moda:wght@500&display=swap" rel="stylesheet">
<style>
  :root{
    --brown:#6b5a2e;
    --sage:#a9a98a;
    --paper:#ffffff;
  }
  *{margin:0;padding:0;box-sizing:border-box;}
  html,body{width:848px;height:1200px;overflow:hidden;background:var(--brown);}
  .menu-page{position:relative;width:848px;height:1200px;font-family:"Poppins",sans-serif;color:var(--brown);}
  .border-pattern{position:absolute;inset:0;background:var(--brown);}
  .sheet{position:absolute;left:44px;top:44px;width:759px;height:1112px;background:var(--paper);border:4px solid var(--sage);}
  .frame{position:absolute;left:0;top:0;width:848px;height:1200px;}
  .brand{position:absolute;left:0;right:0;top:230px;text-align:center;}
  .brand-name{font-weight:600;font-size:70px;letter-spacing:5px;line-height:1;}
  .brand-rule{position:absolute;left:234px;top:324px;width:380px;height:2px;background:var(--brown);border-radius:50%;}
  .brand-tagline{position:absolute;left:0;right:0;top:332px;text-align:center;font-weight:300;font-size:17px;letter-spacing:8px;}
  .section-title{position:absolute;left:343px;top:392px;width:161px;height:31px;background:var(--brown);color:var(--paper);
    font-family:"Bodoni Moda",serif;font-weight:500;font-size:23px;letter-spacing:2px;text-align:center;line-height:32px;border-radius:3px;}
  .row{position:absolute;left:0;width:848px;height:18px;font-size:13.5px;line-height:18px;}
  .row .name{position:absolute;left:126px;top:0;font-weight:700;letter-spacing:1.4px;white-space:nowrap;}
  .row .name-2{top:17px;}
  .row .leader,.row .leader-b{position:absolute;top:13px;height:1px;background:var(--brown);opacity:.75;}
  .row .leader-b{left:595px;width:72px;}
  .row .qty,.row .price,.row .qty-small,.row .price-small{position:absolute;top:0;letter-spacing:1.4px;font-weight:400;}
  .row .qty{left:551px;}
  .row .qty-wide{left:538px;}
  .row .qty-small{left:412px;}
  .row .price-small{left:467px;}
  .row .price{left:682px;}
</style>
</head>
<body>
<div class="menu-page">
  <div class="border-pattern" role="img" aria-label="Decorative scalloped circle pattern in brown and sage"></div>
  <div class="sheet"></div>

  <svg class="frame" viewBox="0 0 848 1200" aria-hidden="true">
    <rect x="62" y="61" width="724" height="1078" fill="none" stroke="var(--sage)" stroke-width="1.5"/>
    <g fill="var(--brown)">
      <polygon points="62,60 126,60 110,76 78,76 78,109 62,125"/>
      <polygon points="786,60 722,60 738,76 770,76 770,109 786,125"/>
      <polygon points="62,1140 126,1140 110,1124 78,1124 78,1091 62,1075"/>
      <polygon points="786,1140 722,1140 738,1124 770,1124 770,1091 786,1075"/>
    </g>
    <g stroke="var(--brown)" stroke-width="1.5">
      <line x1="120" y1="409" x2="343" y2="409"/>
      <line x1="504" y1="409" x2="728" y2="409"/>
      <line x1="120" y1="1095" x2="383" y2="1095"/>
      <line x1="465" y1="1095" x2="728" y2="1095"/>
    </g>
    <g fill="var(--brown)">
      <circle cx="120" cy="409" r="6"/><circle cx="728" cy="409" r="6"/>
      <circle cx="120" cy="1095" r="6"/><circle cx="728" cy="1095" r="6"/>
    </g>
  </svg>
  <svg style="position:absolute;left:384px;top:1084px" width="80" height="22">
    <rect width="80" height="22" rx="11" fill="var(--brown)" opacity=".35" role="img" aria-label="Small flourish ornament"/>
  </svg>

  <div class="brand"><div class="brand-name">NAZANIN</div></div>
  <div class="brand-rule"></div>
  <div class="brand-tagline">PERSIAN RESTAURANT</div>

  <div class="section-title">APERITIF</div>

  <div class="row" style="top:462px"><span class="name">LISETTE WILD BERRY</span><span class="leader" style="left:327px;width:206px"></span><span class="qty">0,2L</span><span class="leader-b"></span><span class="price">9,00</span></div>
  <div class="row" style="top:503px"><span class="name">HUGO</span><span class="leader" style="left:327px;width:206px"></span><span class="qty">0,2L</span><span class="leader-b"></span><span class="price">8,50</span></div>
  <div class="row" style="top:545px"><span class="name">ARANCIO SPRITZ</span><span class="leader" style="left:327px;width:206px"></span><span class="qty">0,2L</span><span class="leader-b"></span><span class="price">8,50</span></div>
  <div class="row" style="top:586px"><span class="name">SEKT ARANCIO</span><span class="leader" style="left:327px;width:206px"></span><span class="qty">0,1L</span><span class="leader-b"></span><span class="price">8,00</span></div>
  <div class="row" style="top:627px"><span class="name">CARDELLO ORANGE</span><span class="leader" style="left:327px;width:206px"></span><span class="qty">0,2L</span><span class="leader-b"></span><span class="price">7,50</span></div>
  <div class="row" style="top:669px"><span class="name">CARDELLO SODA</span><span class="leader" style="left:327px;width:206px"></span><span class="qty">0,2L</span><span class="leader-b"></span><span class="price">7,00</span></div>
  <div class="row" style="top:710px"><span class="name">MARVELLI BIANCO/ROSSO/EXTRA DRY</span><span class="leader" style="left:434px;width:99px"></span><span class="qty">0,2L</span><span class="leader-b"></span><span class="price">7,00</span></div>
  <div class="row" style="top:751px"><span class="name">MAISON DELORME BRUT</span><span class="leader" style="left:329px;width:72px"></span><span class="qty-small">0,2L</span><span class="price-small">25,00</span><span class="qty qty-wide">0,75L</span><span class="leader-b"></span><span class="price">85,00</span></div>
  <div class="row" style="top:792px"><span class="name">MAISON DELORME ROSE</span><span class="leader" style="left:329px;width:72px"></span><span class="qty-small">0,2L</span><span class="price-small">28,00</span><span class="qty qty-wide">0,75L</span><span class="leader-b"></span><span class="price">92,00</span></div>
  <div class="row" style="top:834px"><span class="name">RIESLING SEKT TROCKEN</span><span class="leader" style="left:331px;width:185px"></span><span class="qty qty-wide">0,75L</span><span class="leader-b"></span><span class="price">30,00</span></div>
  <div class="row" style="top:875px"><span class="name">RIESLING SEKT TROCKEN</span><span class="leader" style="left:331px;width:202px"></span><span class="qty">0,1L</span><span class="leader-b"></span><span class="price">8,00</span></div>
  <div class="row" style="top:916px"><span class="name">VON ADLER RIESLING BRUT 2017</span><span class="leader" style="left:382px;width:151px"></span><span class="qty">0,2L</span><span class="leader-b"></span><span class="price">9,00</span></div>
  <div class="row" style="top:958px"><span class="name">BELLAC &amp; ROUSSET- CRÉMANT OPALE</span><span class="name name-2">BRUT VINTAGE LOIRE</span><span class="leader" style="left:445px;width:88px"></span><span class="qty">0,2L</span><span class="leader-b"></span><span class="price">9,00</span></div>
  <div class="row" style="top:1010px"><span class="name">BELLAC &amp; ROUSSET- CRÉMANT ROSÉ</span><span class="name name-2">BRUT PRESTIGE LOIRE</span><span class="leader" style="left:445px;width:88px"></span><span class="qty">0,2L</span><span class="leader-b"></span><span class="price">9,00</span></div>
</div>
</body>
</html>
```